Buch-/eBook-Cover zum Thema Magersucht
Zielgruppe
Ich bin Autorin und suche ein passendes Buchcover. Die Zielgruppe für dieses Buch sind Eltern von magersüchtigen Kindern sowie interessierte medizinische und therapeutische Fachkräfte.
Aufgabenstellung
Bei meinem Buch handelt es sich um einen Ratgeber zur Behandlung von Magersucht bei Kindern und Jugendlichen.
Folgendes muss auf die Vorderseite des Buches:
Titel: Brot baut Brücken
Untertitel: Familienbasierte Pflege bei Magersucht
Ilka Momberg
Ich wünsche mir ein einfühlsames Cover, das die Schwere der Krankheit spiegelt, aber auch die Hoffnung auf Heilung. Bitte keine plumpen Bilder von Waage, Massband oder dünnen Körpern.
Der Klappentext im Word-Dokument ist für die Rückseite des Buchcovers.

```html
<!DOCTYPE html>
<html lang="de">
<head>
<meta charset="utf-8">
<title>Brot baut Brücken – Buchcover</title>
<link rel="stylesheet" href="https://fonts.googleapis.com/css2?family=Roboto:wght@400;700;900&family=Roboto+Condensed:wght@400;500;700&display=swap">
<style>
  :root {
    --navy: #1c2b58;
    --spine: #1b2a57;
    --back-bg: #c5c9d6;
    --white: #ffffff;
    --sky-top: #93b4c8;
    --sky-mid: #cfdfe7;
    --sky-glow: #f6f7f2;
    --figures: #9a978c;
    --wheat-light: #e2c879;
    --wheat: #b29a4e;
    --field: #7d8440;
    --field-dark: #56632c;
  }
  html, body { margin: 0; padding: 0; overflow: hidden; }
  body { width: 1200px; height: 914px; background: var(--back-bg); }
  .cover { position: relative; width: 1200px; height: 914px; overflow: hidden; }

  .back-cover {
    position: absolute; left: 0; top: 0; width: 568px; height: 914px;
    background: var(--back-bg); color: var(--navy);
  }
  .back-title {
    position: absolute; left: 38px; top: 93px; margin: 0;
    font-family: "Roboto Condensed", sans-serif; font-weight: 700;
    font-size: 28px; letter-spacing: 0.3px; line-height: 1;
  }
  .blurb {
    position: absolute; left: 38px; top: 127px; width: 490px;
    font-family: "Roboto", sans-serif; font-size: 16.6px; line-height: 21.6px;
    letter-spacing: 0.55px;
  }
  .blurb p { margin: 0 0 21.6px; }
  .blurb strong { font-weight: 700; }

  .spine {
    position: absolute; left: 568px; top: 0; width: 65px; height: 914px;
    background: var(--spine);
  }
  .spine-text {
    position: absolute; left: 50%; color: var(--white);
    font-family: "Roboto Condensed", sans-serif; font-size: 22px; line-height: 1;
    writing-mode: vertical-rl; transform: translateX(-50%) rotate(180deg);
    white-space: nowrap;
  }
  .spine-title { top: 114px; height: 267px; font-weight: 700; text-align: end; }
  .spine-author { top: 420px; height: 195px; font-weight: 400; letter-spacing: 0.5px; text-align: end; }

  .front-cover {
    position: absolute; left: 633px; top: 0; width: 567px; height: 914px;
    color: var(--navy); text-align: center;
  }
  .front-photo {
    position: absolute; inset: 0;
    background:
      radial-gradient(ellipse 60% 12% at 80% 58%, rgba(255,255,250,0.9), rgba(255,255,250,0) 100%),
      linear-gradient(180deg, rgba(0,0,0,0) 48%, rgba(154,151,140,0.35) 56%, rgba(154,151,140,0.5) 64%, rgba(0,0,0,0) 72%),
      linear-gradient(180deg, var(--sky-top) 0%, var(--sky-mid) 30%, var(--sky-glow) 52%, var(--wheat-light) 68%, var(--wheat) 78%, var(--field) 90%, var(--field-dark) 100%);
  }
  .front-author {
    position: absolute; left: 0; right: 0; top: 35px; margin: 0;
    font-family: "Roboto Condensed", sans-serif; font-weight: 400;
    font-size: 29px; letter-spacing: 0.6px; line-height: 1;
  }
  .front-title { margin: 0; font-family: "Roboto", sans-serif; font-weight: 900; }
  .front-title span {
    position: absolute; left: 0; right: 0; display: block; line-height: 1;
  }
  .title-line-1 { top: 99px; font-size: 100px; letter-spacing: -1px; }
  .title-line-2 { top: 194px; font-size: 50px; }
  .title-line-3 { top: 241px; font-size: 100px; letter-spacing: -1px; }
  .front-subtitle {
    position: absolute; left: 0; right: 0; top: 343px; margin: 0;
    font-family: "Roboto Condensed", sans-serif; font-weight: 400;
    font-size: 34px; line-height: 41px; letter-spacing: 0.3px;
  }
</style>
</head>
<body>
<main class="cover">
  <section class="back-cover">
    <h2 class="back-title">BROT BAUT BRÜCKEN</h2>
    <div class="blurb">
      <p>Anorexia Nervosa - Magersucht - ist eine genetisch veranlagte, psychobiologische Krankheit mit einer Sterberate von 10-15%. Je früher die Krankheit diagnostiziert wird, je jünger die Patient:innen bei der Diagnose sind, je rascher mit der Wiederernährung begonnen wird und je schneller ein individuelles gesundes Gewicht erreicht wird, desto grösser ist die langfristige Heilungschance.</p>
      <p>Bei Kindern und Jugendlichen ist gemäß der modernen Anorexie-Forschung die Familie nicht das Problem, sondern in der Regel die größte Ressource für die Heilung. Bei der familienbasierten Pflege zuhause steht die rasche Wiederherstellung des gesunden Gewichts im Vordergrund. Die Eltern übernehmen die volle Verantwortung für die Wiederernährung ihres kranken Kindes, bis sich dessen Verhalten normalisiert hat.</p>
      <p>Dieser Ratgeber liefert ein tiefes Verständnis für die Krankheit auf Basis moderner wissenschaftlicher Erkenntnisse. Er unterstützt Eltern in der Pflege ihrer Kinder zuhause anhand zahlreicher Tipps und erprobter Praxisbeispiele. Von Kochrezepten über den Umgang mit Angst, Aggression und Essensverweigerung bis hin zum Thema Selbstfürsorge ist er eine unentbehrliche Quelle für alle Eltern, die ihre Kinder in die Genesung begleiten möchten. <strong>Anorexie ist heilbar.</strong></p>
    </div>
  </section>

  <section class="spine">
    <span class="spine-text spine-title">BROT BAUT BRÜCKEN</span>
    <span class="spine-text spine-author">ILKA MOMBERG</span>
  </section>

  <section class="front-cover">
    <div class="front-photo" role="img" aria-label="Foto: vierköpfige Familie von hinten, Hand in Hand in einem goldenen Weizenfeld im Gegenlicht der Abendsonne unter hellblauem Himmel"></div>
    <p class="front-author">ILKA MOMBERG</p>
    <h1 class="front-title">
      <span class="title-line-1">BROT</span>
      <span class="title-line-2">BAUT</span>
      <span class="title-line-3">BRÜCKEN</span>
    </h1>
    <p class="front-subtitle">Familienbasierte Pflege<br>bei Magersucht</p>
  </section>
</main>
</body>
</html>
```